Law Office needs stationery design and business card

I currently have been using the same letterhead for the last 8 years. Since i 'm about to adding another location, I want to revamp my letterhead and business card. I already have a logo i'm happy with. I will upload my current letterhead, fax sheet, envelope, and logos. I need a business card also. I have 2 locations, 1 phone number, 1 fax line, website, etc. If possible and fitting with the design, I would like to keep the same information listed currently on the letterhead.

**Keep in mind, I also NEED A FAX SHEET COVER. thank you

Hello, Please submit a Gray Scale or Black and White version of your designs also, since most of the time I will be printing NON color stationery. I will seldom use a color print for my letterhead, I would like to have a color version for my benefit, however i will print in grayscale majority of the time . For the Business Card, that can just be in color. When I get my business cards they will be in color.Thank youEnrique Added Sunday, September 18, 2016

```html
<!DOCTYPE html>
<html lang="en">
<head>
<meta charset="utf-8">
<title>Carveth Law Stationery</title>
<link href="https://fonts.googleapis.com/css2?family=Cinzel:wght@700&family=Open+Sans:wght@400;600&display=swap" rel="stylesheet">
<style>
  :root {
    --navy: #0d2f6b;
    --grey-dark: #4a4a4a;
    --grey-mid: #a5a5a5;
    --grey-faint: #e8e8e8;
    --backdrop: #939393;
    --paper: #ffffff;
    --ink: #222222;
  }
  * { margin: 0; padding: 0; box-sizing: border-box; }
  html, body { width: 1200px; height: 1200px; overflow: hidden; }
  body { background: var(--backdrop); position: relative; font-family: "Open Sans", Arial, sans-serif; color: var(--ink); }
  .sheet { position: absolute; background: var(--paper); overflow: hidden; }
  .brand-name { font-family: "Cinzel", Georgia, serif; font-weight: 700; color: var(--navy); letter-spacing: 0.02em; white-space: nowrap; }
  .brand-square { position: absolute; background: var(--navy); }
  .faint-square { position: absolute; background: var(--grey-faint); }
  .contact { position: absolute; font-size: 8.5px; line-height: 1.3; color: #333; }
  .contact b { color: var(--navy); font-weight: 600; }
  .band { position: absolute; left: 0; right: 0; }
  .band-navy { position: absolute; left: 0; top: 0; bottom: 0; background: var(--navy); clip-path: polygon(0 0, 100% 0, calc(100% - 18px) 100%, 0 100%); }
  .band-grey { position: absolute; right: 0; top: 0; bottom: 0; background: var(--grey-dark); clip-path: polygon(18px 0, 100% 0, 100% 100%, 0 100%); display: flex; align-items: center; justify-content: flex-end; padding-right: 34px; }
  .web { color: #fff; font-size: 10px; letter-spacing: 0.45em; font-style: italic; }

  /* Logo sheet */
  .logo-sheet { left: 41px; top: 26px; width: 1118px; height: 418px; }
  .logo-sheet .brand-square { left: 469px; top: 94px; width: 180px; height: 180px; }
  .logo-sheet .brand-name { position: absolute; left: 0; right: 0; top: 322px; text-align: center; font-size: 52px; }

  /* Business card front */
  .card-front { left: 41px; top: 460px; width: 286px; height: 174px; }
  .card-front .brand-square { left: 123px; top: 20px; width: 40px; height: 40px; }
  .card-front .brand-name { position: absolute; left: 0; right: 0; top: 78px; text-align: center; font-size: 14px; }
  .holder { position: absolute; right: 150px; top: 110px; text-align: right; line-height: 1.15; }
  .holder-name { font-size: 13px; color: var(--navy); }
  .holder-role, .holder-addr { font-size: 7px; color: #444; }
  .card-divider { position: absolute; left: 145px; top: 110px; width: 1px; height: 36px; background: #999; }
  .card-front .contact { left: 152px; top: 109px; font-size: 7px; }
  .card-front .band { bottom: 0; height: 14px; }
  .card-front .band-navy { width: 170px; }
  .card-front .band-grey { width: 128px; }

  /* Business card back */
  .card-back { left: 342px; top: 460px; width: 287px; height: 174px; background: var(--navy); }
  .card-back .brand-square { left: 121px; top: 36px; width: 44px; height: 44px; background: var(--paper); }
  .card-back .brand-name { position: absolute; left: 0; right: 0; top: 112px; text-align: center; font-size: 16px; color: var(--paper); }

  /* Envelope */
  .envelope { left: 41px; top: 654px; width: 588px; height: 252px; }
  .envelope .faint-square { left: 330px; top: 40px; width: 170px; height: 170px; }
  .envelope .brand-square { left: 56px; top: 34px; width: 46px; height: 46px; }
  .envelope .brand-name { position: absolute; left: 16px; top: 90px; font-size: 16px; }
  .envelope .contact { left: 457px; top: 16px; }
  .envelope .band { bottom: 0; height: 20px; }
  .envelope .band-navy { width: 330px; }
  .envelope .band-grey { width: 276px; }

  /* Envelope back */
  .envelope-back { left: 41px; top: 930px; width: 588px; height: 258px; }
  .envelope-back svg { position: absolute; left: 0; top: 0; }
  .envelope-back .brand-square { left: 277px; top: 16px; width: 34px; height: 34px; background: var(--paper); }
  .envelope-back .brand-name { position: absolute; left: 0; right: 0; top: 56px; text-align: center; font-size: 11px; color: var(--paper); }

  /* Letterhead */
  .letterhead { left: 644px; top: 460px; width: 515px; height: 728px; }
  .letterhead .faint-square { left: 176px; top: 280px; width: 190px; height: 190px; }
  .letterhead .brand-square { left: 92px; top: 36px; width: 54px; height: 54px; }
  .letterhead .brand-name { position: absolute; left: 26px; top: 106px; font-size: 18px; }
  .letterhead .contact { left: 389px; top: 14px; }
  .letter { position: absolute; left: 46px; top: 180px; width: 424px; font-size: 11px; line-height: 1.3; }
  .letter p { margin-bottom: 14px; }
  .letter .address { line-height: 1.45; }
  .letter .body { text-align: justify; font-size: 11.4px; line-height: 1.8; margin-bottom: 6px; }
  .letter .signature { font-weight: 600; }
  .letterhead .band { bottom: 8px; height: 20px; }
  .letterhead .band-navy { width: 296px; }
  .letterhead .band-grey { width: 232px; }
</style>
</head>
<body>

<section class="sheet logo-sheet">
  <div class="brand-square"></div>
  <div class="brand-name">CARVETH LAW</div>
</section>

<section class="sheet card-front">
  <div class="brand-square"></div>
  <div class="brand-name">CARVETH LAW</div>
  <div class="holder">
    <div class="holder-name">Your Name</div>
    <div class="holder-role">Manager</div>
    <div class="holder-addr">0000 Elm Point<br>USA</div>
  </div>
  <div class="card-divider"></div>
  <div class="contact">
    <b>P</b> : 0100-555-200<br>
    <b>C</b> : 0100-555-201<br>
    <b>F</b> : 0100-555-202<br>
    <b>E</b> : office@carveth.law
  </div>
  <div class="band"><div class="band-navy"></div><div class="band-grey"></div></div>
</section>

<section class="sheet card-back">
  <div class="brand-square"></div>
  <div class="brand-name">CARVETH LAW</div>
</section>

<section class="sheet envelope">
  <div class="faint-square"></div>
  <div class="brand-square"></div>
  <div class="brand-name">CARVETH LAW</div>
  <div class="contact">
    14 Harlow Dr Fairview, TX 75010<br>
    <b>P</b> : 0100-555-200<br>
    <b>C</b> : 0100-555-201<br>
    <b>F</b> : 0100-555-202<br>
    <b>E</b> : office@carveth.law
  </div>
  <div class="band"><div class="band-navy"></div><div class="band-grey"><span class="web">www.carvethlaw.com</span></div></div>
</section>

<section class="sheet envelope-back">
  <svg width="588" height="120" viewBox="0 0 588 120" aria-hidden="true">
    <path d="M0,0 H588 C584,20 580,36 562,44 Q294,124 26,44 C8,36 4,20 0,0 Z" fill="var(--navy)"/>
  </svg>
  <div class="brand-square"></div>
  <div class="brand-name">CARVETH LAW</div>
</section>

<section class="sheet letterhead">
  <div class="faint-square"></div>
  <div class="brand-square"></div>
  <div class="brand-name">CARVETH LAW</div>
  <div class="contact">
    14 Harlow Dr Fairview, TX 75010<br>
    <b>P</b> : 0100-555-200<br>
    <b>C</b> : 0100-555-201<br>
    <b>F</b> : 0100-555-202<br>
    <b>E</b> : office@carveth.law
  </div>
  <div class="letter">
    <p>Date</p>
    <p>Recipient Name</p>
    <p class="address">Company Name<br>Street Address<br>City, State, Zip</p>
    <p class="body">This is the template of the letterhead of the official Example club. The typeface used is Arial 10.5 pt with 12.5 pt line spacing. This text is so-called dummy text and has no meaning. This dummy text is not meant to be read. Its only purpose is to demonstrate the size, colour and position of the text within the correct format. The typeface used is Arial 10.5 pt with 12.5 pt line spacing. This text is so-called dummy text and has no meaning. This dummy text is not meant to be read. Its only purpose is to demonstrate the size, colour and position of the text within the correct format. The typeface used is Arial 10.5 pt with 12.5 pt line spacing. This text is so-called dummy text and has no meaning</p>
    <p>It only purpose is to demonstrate the size, colour and position of the text within the correct format.</p>
    <p>Yours Sincerely,</p>
    <p class="signature">Sample</p>
  </div>
  <div class="band"><div class="band-navy"></div><div class="band-grey"><span class="web">www.carvethlaw.com</span></div></div>
</section>

</body>
</html>
```